Restaurant service company needs a website!

I am looking for a skilled web designer/developer to create a professional, responsive, and easy-to-navigate website for my company, which specializes in servicing restaurant cooking equipment. The site should communicate trust, reliability, and technical expertise to our target audience, restaurant owners, managers, and commercial kitchen operators. I have included the company logos, if any other format for them is needed please let me know.

Target Market(s)

restaurant owners, managers, and commercial kitchen operators

Industry/Entity Type

Commercial Kitchen Equipment Service

Coding

Coded - Design and coding required

Number of Pages Required

1 page

Font styles to use
Serif
Sans Serif

Requirements
Must have
• Contact and service request forms, Click-to-call functionality for mobile, Clean, modern layout with strong visuals, Easy navigation, mobile-friendly
Nice to have
• Testimonials or Reviews, If possible a click-to-text functionality for mobile.
Should not have
• Any mention of Refrigeration or HVAC, "Free Quotes"

```html
<!DOCTYPE html>
<html lang="en">
<head>
<meta charset="utf-8">
<title>Hearthline Kitchen Services</title>
<link href="https://fonts.googleapis.com/css2?family=Plus+Jakarta+Sans:wght@500;600;700&family=Inter:wght@400;500;600&display=swap" rel="stylesheet">
<style>
:root{
  --teal:#0d6a88;
  --teal-dark:#0f5a72;
  --teal-soft:#dce9ed;
  --slate:#4f7d91;
  --ink:#161a1d;
  --text:#3a3f44;
  --muted:#7b8287;
  --line:#e3e5e7;
  --hero-bg:#eceeec;
  --pale:#f4f5f7;
  --field:#faf6ef;
  --white:#fff;
}
*{box-sizing:border-box;margin:0;padding:0}
html,body{width:1200px;height:4739px;overflow:hidden}
body{position:relative;background:var(--white);font-family:"Inter",sans-serif;color:var(--text);font-size:10px;line-height:1.6}
.abs{position:absolute}
h1,h2,h3,.display{font-family:"Plus Jakarta Sans",sans-serif;color:var(--ink);letter-spacing:-0.03em;font-weight:700}
.photo{position:absolute;display:block}
.eyebrow{font-size:10px;color:var(--muted);text-align:center}
.section-title{font-size:24px;text-align:center;font-weight:600}
.btn{display:inline-block;background:var(--teal);color:#fff;border-radius:20px;font-size:9px;font-weight:600;padding:7px 14px;text-decoration:none}
.link-line{font-size:9px;font-weight:600;color:var(--ink);text-decoration:none;border-bottom:1.5px solid var(--ink);padding-bottom:6px;display:inline-block;width:70px;text-align:center}

/* header */
.site-header{top:0;left:0;width:1200px;height:65px}
.brand{top:20px;left:195px;display:flex;align-items:center;gap:6px}
.brand-mark{width:10px;height:10px;border:2px solid var(--teal)}
.brand-name{font-family:"Plus Jakarta Sans",sans-serif;font-weight:700;font-size:13px;color:var(--teal);letter-spacing:.02em}
.nav{top:25px;left:362px;display:flex;gap:18px;font-size:9.5px;font-weight:600;color:var(--ink)}
.call{top:24px;left:758px;font-size:9.5px;font-weight:600;color:var(--ink)}
.cart{top:17px;left:882px;width:30px;height:30px;border-radius:50%;background:#eef0f1;display:flex;align-items:center;justify-content:center}
.quote{top:16px;left:925px;padding:8px 14px}

/* hero */
.hero{top:65px;left:0;width:1200px;height:425px;background:var(--hero-bg)}
.hero h1{position:absolute;top:62px;left:193px;font-size:32px;line-height:1.15;width:400px}
.hero p{position:absolute;top:148px;left:193px;width:290px;font-size:9.5px}
.stat{position:absolute;left:193px;display:flex;align-items:center;gap:12px}
.stat b{font-family:"Plus Jakarta Sans",sans-serif;font-size:20px;color:var(--ink);width:36px}
.stat span{font-size:9.5px;line-height:1.5}

/* service cards */
.svc-card{top:623px;width:262px;height:244px;border-radius:4px;overflow:hidden}
.svc-card .cap{position:absolute;left:18px;bottom:22px;color:#fff}
.svc-card h3{color:#fff;font-size:15px;font-weight:600;letter-spacing:-.01em}
.svc-card small{font-size:9px;opacity:.9}

/* process */
.step{top:1015px;width:240px}
.step h3{font-size:14px;font-weight:600;margin:8px 0 6px;letter-spacing:-.01em}
.step p{font-size:9.5px}

/* interior */
.interior-copy{top:1275px;left:614px;width:330px}
.interior-copy .label{font-size:10px;color:var(--muted)}
.interior-copy h2{color:var(--teal);font-size:24px;line-height:1.15;margin:6px 0 14px}
.interior-copy p{font-size:9.5px;margin-bottom:18px}

/* affordable */
.afford{top:2073px;left:193px;width:262px;height:363px;background:var(--teal-soft);border-radius:0 0 70px 0;padding:60px 24px 0}
.afford .label{font-size:10px;color:var(--muted)}
.afford h2{color:var(--teal);font-size:23px;line-height:1.12;margin:6px 0 18px;font-weight:600}
.afford p{font-size:9.5px;margin-bottom:16px}

.brands{top:2465px;left:193px;width:813px;display:flex;justify-content:space-between}
.brands span{font-family:"Plus Jakarta Sans",sans-serif;font-weight:700;font-size:15px;color:#333;width:110px;text-align:center}

.featured{top:2590px;left:193px;width:813px;border-bottom:1px solid var(--line);height:36px}
.featured h2{font-size:22px;font-weight:600}
.featured a{position:absolute;right:0;top:6px;font-size:9px;font-weight:600;color:var(--ink);border-bottom:2px solid var(--ink);padding-bottom:6px;text-decoration:none;width:62px;text-align:center}

.promo{top:2715px;width:600px;height:313px}
.promo .copy{position:absolute;left:78px;top:82px}
.promo .copy small{font-size:9.5px}
.promo h2{font-size:32px;line-height:1.15;margin:10px 0 16px;font-weight:600}

/* testimonials */
.testi{top:3028px;left:0;width:1200px;height:437px;background:var(--pale)}
.t-card{top:3165px;left:256px;width:750px;height:215px;background:#fff;border-radius:14px}
.t-card p{position:absolute;top:60px;left:81px;width:610px;font-size:10.5px;line-height:1.75;color:var(--ink)}
.t-card .who{position:absolute;top:138px;left:81px;font-size:9.5px;font-weight:600;color:var(--ink);display:flex;align-items:center;gap:10px}
.t-card .who::before{content:"";width:24px;height:1px;background:var(--ink)}
.avatar{top:3216px;left:197px;width:98px;height:98px;border-radius:50%;border:4px solid #fff;background:linear-gradient(160deg,#c9d3da,#5c7d93)}

/* contact */
.contact{top:3538px;left:193px;width:400px}
.contact h2{font-size:17px;font-weight:600;margin-bottom:10px}
.contact p{font-size:9.5px;line-height:1.75}
.info{position:absolute;display:flex;gap:14px;font-size:9.5px}
.info b{display:block;font-size:9px;font-weight:600;color:var(--ink)}
.form{top:3560px;left:612px;width:394px}
.field{position:absolute;font-size:9.5px;font-weight:600;color:var(--ink)}
.field i{display:block;margin-top:8px;height:28px;background:var(--field);border-radius:2px;font-style:normal}
.field i.msg{height:55px;font-weight:400;color:var(--muted);padding:8px 10px;font-size:9px}

/* blog */
.post{left:193px;width:740px;height:72px;display:flex;align-items:center}
.post .date{width:52px;font-size:8px;line-height:1.2;color:var(--ink)}
.post .date b{display:block;font-size:16px;font-family:"Plus Jakarta Sans",sans-serif}
.post .thumb{width:40px;height:40px;border-radius:50%;margin-right:20px}
.post h3{font-size:13.5px;font-weight:600;width:485px;letter-spacing:-.01em}
.post .cat{font-size:7.5px;color:var(--muted);width:80px}
.post a{font-size:9px;color:var(--teal);text-decoration:none}

/* footer */
.footer{top:4505px;left:0;width:1200px;height:234px;background:var(--teal-dark);color:#dfe9ee}
.footer .col{position:absolute;top:74px;font-size:9.5px;line-height:1.85}
.footer .col b{display:block;font-size:9px;font-weight:600;color:#fff;margin-bottom:6px}
.social{display:flex;gap:6px;margin-top:8px}
.social i{width:9px;height:9px;border-radius:50%;background:#cfe0e6;display:block}
</style>
</head>
<body>

<header class="abs site-header">
  <div class="abs brand"><span class="brand-mark"></span><span class="brand-name">HEARTHLINE</span></div>
  <nav class="abs nav"><span>Home ⌄</span><span>About</span><span>Shop ⌄</span><span>Services ⌄</span><span>Blog ⌄</span><span>Contact</span></nav>
  <div class="abs call">Call us: 05 210 447 318</div>
  <div class="abs cart"><svg width="13" height="13" viewBox="0 0 24 24" fill="none" stroke="#222" stroke-width="2"><path d="M3 4h3l2 11h11l2-8H7"/><circle cx="10" cy="20" r="1.5"/><circle cx="18" cy="20" r="1.5"/></svg></div>
  <a class="abs btn quote">GET A QUOTE</a>
</header>

<section class="abs hero">
  <h1>Commercial Kitchen with International Quality</h1>
  <p>With over 20 years of experience in providing reliable, top-tier kitchen equipment, we deliver quality, innovation, and customer service that restaurant owners trust. where quality transcends borders and sophistication is truly international.</p>
  <div class="stat" style="top:302px"><b>61+</b><span>Completed<br>Projects</span></div>
  <div class="stat" style="top:350px"><b>15+</b><span>Years in the<br>Industry</span></div>
  <div class="photo" role="img" aria-label="Chef with arms crossed in a commercial kitchen" style="left:350px;top:253px;width:250px;height:172px;background:linear-gradient(135deg,#cfd5d8,#6d7a82)"></div>
  <div class="photo" role="img" aria-label="Modern stainless steel commercial kitchen" style="left:600px;top:0;width:406px;height:425px;background:linear-gradient(170deg,#2f3a44,#8a98a3 55%,#c9d0d4)"></div>
</section>

<div class="abs eyebrow" style="top:550px;left:0;width:1200px">We serve multiple</div>
<h2 class="abs section-title" style="top:568px;left:0;width:1200px">Ultimate Services</h2>

<div class="abs svc-card" style="left:193px"><div class="photo" role="img" aria-label="Hand holding a kitchen design model" style="inset:0;background:linear-gradient(180deg,#c8cbce,#55595d 75%,#2b2e31)"></div><div class="cap"><h3>Custom Design</h3><small>Elevate Your Space with Tailored Custom Designs.</small></div></div>
<div class="abs svc-card" style="left:469px"><div class="photo" role="img" aria-label="Installed commercial kitchen with steel hood" style="inset:0;background:linear-gradient(180deg,#6d7880,#3b4349 70%,#1f2428)"></div><div class="cap"><h3>Precise Installation</h3><small>Flawless Installation for a Polished Look.</small></div></div>
<div class="abs svc-card" style="left:745px"><div class="photo" role="img" aria-label="Chef cooking in a remodeled kitchen" style="inset:0;background:linear-gradient(180deg,#3c6d78,#2b4a52 65%,#1b2a2e)"></div><div class="cap"><h3>Remodeling</h3><small>Transform Your Home with Expert Services.</small></div></div>

<div class="abs" style="top:946px;left:0;width:1200px;text-align:center;font-size:8px;color:var(--teal);font-weight:600">– OUR PROCESS –</div>
<h2 class="abs section-title" style="top:962px;left:0;width:1200px">Freedom and flexibility</h2>

<div class="abs step" style="left:193px">
  <svg width="38" height="38" viewBox="0 0 40 40" fill="none" stroke="#222" stroke-width="2"><path d="M10 36V22c-4-2-5-8 0-11 2-6 12-8 16-2 6 0 9 7 4 12v15z"/><path d="M10 30h20"/></svg>
  <h3>Consultation</h3><p>Schedule a visit for measurements and discuss your garage door preferences in detail.</p>
</div>
<div class="abs step" style="left:472px">
  <svg width="38" height="38" viewBox="0 0 40 40" fill="none" stroke="#222" stroke-width="2"><rect x="4" y="10" width="26" height="20" rx="8"/><path d="M30 16h4a4 4 0 010 8h-4M10 34h16"/></svg>
  <h3>Delivery</h3><p>Choose your door style and features you want, and we will prepare everything for installation.</p>
</div>
<div class="abs step" style="left:751px">
  <svg width="38" height="38" viewBox="0 0 40 40" fill="none" stroke="#222" stroke-width="2"><rect x="6" y="8" width="28" height="28"/><rect x="11" y="13" width="18" height="10"/><path d="M11 29h4M19 29h4M27 29h2M12 4h16"/></svg>
  <h3>Support</h3><p>Schedule a visit for maintenance and discuss your garage door preferences in detail.</p>
</div>

<div class="photo" role="img" aria-label="Chef plating a dish" style="left:193px;top:1204px;width:120px;height:148px;background:linear-gradient(160deg,#3a4147,#a4672f 70%,#2a2f33)"></div>
<div class="photo" role="img" aria-label="Wooden kitchen cabinetry" style="left:193px;top:1368px;width:120px;height:148px;background:linear-gradient(160deg,#6b7567,#c9ad8a 60%,#8d7760)"></div>
<div class="photo" role="img" aria-label="Restaurant dining room with teal banquettes" style="left:329px;top:1204px;width:256px;height:312px;background:linear-gradient(180deg,#2d4b54,#7a8c8e 45%,#e3dad2)"></div>
<div class="abs interior-copy">
  <div class="label">Interior Decoration</div>
  <h2>Interior Decoration party Thrives on Being Social.</h2>
  <p>With years of experience and a passion for design, we specialize in creating stunning kitchens that combine functionality and style.</p>
  <a class="btn">Explore Products</a>&nbsp;&nbsp;&nbsp;&nbsp;&nbsp;<a class="link-line">Contact Us</a>
</div>

<div class="photo" role="img" aria-label="Wide view of a restaurant with pink chairs and teal booths" style="left:0;top:1578px;width:1200px;height:362px;background:linear-gradient(170deg,#25323a,#6f6b67 35%,#d9c9c2 65%,#8a7e74)"></div>

<div class="abs eyebrow" style="top:2000px;left:0;width:1200px">We serve multiple</div>
<h2 class="abs section-title" style="top:2018px;left:0;width:1200px">Ultimate Services</h2>

<div class="abs afford">
  <div class="label">Interior Decoration</div>
  <h2>Affordable Commercial &amp; Restaurant Equipment</h2>
  <p>With years of experience and a passion for design, we specialize in creating stunning functionality and style.</p>
  <a class="btn">Explore Products</a>&nbsp;&nbsp;&nbsp;<a class="link-line">Contact Us</a>
</div>
<div class="photo" role="img" aria-label="Chef cooking on a commercial range" style="left:469px;top:2073px;width:261px;height:363px;border-radius:0 70px 0 0;background:linear-gradient(170deg,#d2d4d5,#6a6f72 55%,#3a3d40)"></div>
<div class="photo" role="img" aria-label="Gas burners on a black cooktop" style="left:745px;top:2073px;width:261px;height:363px;border-radius:70px 0 0 0;background:linear-gradient(180deg,#1b1c1d,#55575a 55%,#111)"></div>

<div class="abs brands"><span>norvane</span><span>kelto</span><span>● ombra</span><span>Veltris</span><span style="font-size:12px;letter-spacing:.08em">AUREXA</span><span style="font-style:normal;letter-spacing:.1em;font-size:12px">PALLOR</span></div>

<div class="abs featured"><h2>Featured Products</h2><a>Best seller</a></div>

<section class="abs promo" style="left:0;background:#e4e6e8">
  <div class="photo" role="img" aria-label="Barista working at an espresso machine" style="left:250px;top:0;width:350px;height:313px;background:linear-gradient(90deg,#e4e6e8,#a49a91 50%,#5e5a57)"></div>
  <div class="copy"><small>Bring your vision to life.</small><h2>Coffee Shop<br>Equipment</h2><a class="btn">View Collection</a></div>
</section>
<section class="abs promo" style="left:600px;background:var(--slate)">
  <div class="photo" role="img" aria-label="Chef holding a bowl of salad in a kitchen" style="left:250px;top:0;width:350px;height:313px;background:linear-gradient(90deg,var(--slate),#8e9da6 55%,#c8d0d4)"></div>
  <div class="copy" style="color:#e8eff2"><small>Bring your vision to life.</small><h2 style="color:#fff">Commercial<br>Kitchen</h2><a class="btn">View Collection</a></div>
</section>

<section class="abs testi"></section>
<div class="abs eyebrow" style="top:3090px;left:0;width:1200px">Be inspired to meet</div>
<h2 class="abs section-title" style="top:3106px;left:0;width:1200px">Client Testimonials</h2>
<div class="abs t-card">
  <p>I was amazed by the creativity in their custom designs. The installation was smooth, and the remodeling breathed new life into my living area. Their custom designs brought a new level of sophistication to my home. The installation was flawless, and the remodeling truly revitalized the space.</p>
  <div class="who">MARCUS ELLERY</div>
  <div class="abs" style="left:672px;top:180px;font-size:12px;color:var(--ink)">← →</div>
</div>
<div class="abs avatar" role="img" aria-label="Client portrait"></div>

<div class="abs contact">
  <h2>Get in touch</h2>
  <p>Thank you for your interest in our services! If you have any questions or would like to book a service, please don't hesitate to contact us. Our team is dedicated to providing you with the highest level of service and support, and we are committed to working with you to make your event a success.</p>
</div>
<div class="info" style="top:3662px;left:193px">
  <svg width="26" height="26" viewBox="0 0 26 26" fill="none" stroke="#333" stroke-width="1.5"><rect x="2" y="5" width="22" height="16"/><circle cx="13" cy="13" r="4"/></svg>
  <div><b>EMAIL ADDRESS</b>service@hearthline-kitchens.com</div>
</div>
<div class="info" style="top:3662px;left:398px">
  <svg width="26" height="26" viewBox="0 0 26 26" fill="none" stroke="#333" stroke-width="1.5"><circle cx="9" cy="9" r="4"/><circle cx="18" cy="9" r="3"/><path d="M2 22c0-5 4-8 7-8s7 3 7 8M16 14c4 0 8 3 8 8"/></svg>
  <div><b>PHONE NUMBER</b>+31 204 118 552 – Office</div>
</div>
<div class="info" style="top:3712px;left:193px">
  <svg width="26" height="26" viewBox="0 0 26 26" fill="none" stroke="#333" stroke-width="1.5"><path d="M13 24s-7-7-7-13a7 7 0 0114 0c0 6-7 13-7 13z"/><circle cx="13" cy="11" r="2.5"/></svg>
  <div><b>OUR ADDRESS</b>1820 Harbor Mill Road, NY City</div>
</div>

<div class="abs form">
  <div class="field" style="left:20px;top:24px;width:170px">Last Name (required)<i></i></div>
  <div class="field" style="left:202px;top:24px;width:170px">First Name (required)<i></i></div>
  <div class="field" style="left:20px;top:90px;width:170px">Your Phone (required)<i></i></div>
  <div class="field" style="left:202px;top:90px;width:170px">Your Email (required)<i></i></div>
  <div class="field" style="left:20px;top:156px;width:352px">Your Message (required)<i class="msg">Message</i></div>
</div>

<div class="photo" role="img" aria-label="Map showing office locations along the Gulf coast" style="left:10px;top:3805px;width:1180px;height:275px;background:linear-gradient(180deg,#eef0ec 0%,#e8ebe5 55%,#b6dde8 80%,#a9d6e4)"></div>

<div class="abs eyebrow" style="top:4142px;left:0;width:1200px">Recent updates</div>
<h2 class="abs section-title" style="top:4160px;left:0;width:1200px">Our Latest Blog Posts</h2>

<div class="abs post" style="top:4215px;border-bottom:1px solid var(--line)">
  <div class="date">October<b>31</b></div><div class="thumb" role="img" aria-label="Kitchen tools" style="background:linear-gradient(135deg,#a7b39a,#4e5a45)"></div>
  <h3>Precision and Performance: The Essential Tools Every Chef Needs</h3><span class="cat">UNCATEGORIZED</span><a>Read more</a>
</div>
<div class="abs post" style="top:4296px;border-bottom:1px solid var(--line)">
  <div class="date">October<b>31</b></div><div class="thumb" role="img" aria-label="Chef knives on a board" style="background:linear-gradient(135deg,#c8a880,#4a3f36)"></div>
  <h3>From Blades to Boards: Your Guide to Professional Chef Equipment</h3><span class="cat">UNCATEGORIZED</span><a>Read more</a>
</div>
<div class="abs post" style="top:4377px">
  <div class="date">October<b>31</b></div><div class="thumb" role="img" aria-label="Prepared dish" style="background:linear-gradient(135deg,#d9b27a,#7a5532)"></div>
  <h3>Equipping the Masters: Must-Have Tools for Culinary Excellence</h3><span class="cat">UNCATEGORIZED</span><a>Read more</a>
</div>

<footer class="abs footer">
  <div class="col" style="left:193px;top:80px">
    <div style="display:flex;align-items:center;gap:6px"><span class="brand-mark" style="border-color:#fff"></span><span class="brand-name" style="color:#fff">HEARTHLINE</span></div>
    <div class="social"><i></i><i></i><i></i><i></i><i></i></div>
  </div>
  <div class="col" style="left:400px"><b>NEW YORK</b>412 Larkspur Ave, 3rd Floor<br>New York, 1180 NYC<br><b style="margin-top:10px">LONDON</b>77 Fenwick Row, 5th Floor<br>London, 4410 UK</div>
  <div class="col" style="left:607px"><b>FOOTER MENU</b>Home<br>Blog<br>About<br>Shop<br>Contact us</div>
  <div class="col" style="left:814px"><b>FOOTER MENU</b>Home<br>Blog<br>Shop<br>About<br>Contact us</div>
</footer>

</body>
</html>
```